The Plaster & Resonance Craftworks Inc (PRCI)

Create a LOGO and Business Card design.

Colors: Black, Bright Yellow & Red

Description of company: commercial carpentry, metal framing, drywall, taping/spackling, demolition, rough/finish carpentry.

Target Market(s)

developers, architects, general contractors, construction managers

Industry/Entity Type

Business

```html
<!DOCTYPE html>
<html lang="en">
<head>
<meta charset="utf-8">
<title>PRCI Business Card</title>
<link rel="stylesheet" href="https://fonts.googleapis.com/css2?family=Didact+Gothic&family=Tinos&family=Arimo&display=swap">
<style>
  :root {
    --backdrop: #dcdcdc;
    --card: #ffffff;
    --brand-red: #d40f0f;
    --ink: #111111;
    --card-shadow: 0 6px 18px rgba(0,0,0,0.18);
  }
  * { margin: 0; padding: 0; box-sizing: border-box; }
  html, body {
    width: 1200px; height: 900px; overflow: hidden;
    background: var(--backdrop);
  }
  .canvas { position: relative; width: 1200px; height: 900px; }
  .card {
    position: absolute; width: 640px; height: 380px;
    background: var(--card); border-radius: 18px; overflow: hidden;
    box-shadow: var(--card-shadow);
  }
  .card--front { left: 70px; top: 60px; }
  .card--back { left: 490px; top: 460px; }

  .edge-bar { position: absolute; width: 14px; height: 150px; background: var(--brand-red); }
  .edge-bar--left { left: 20px; top: 175px; }
  .edge-bar--right { right: 20px; top: 110px; }

  .wordmark {
    font-family: "Didact Gothic", sans-serif;
    color: var(--ink); letter-spacing: 0.5em; line-height: 1;
  }
  .tagline { font-family: "Didact Gothic", sans-serif; color: var(--ink); }

  .card--front .brand { position: absolute; left: 0; right: 0; top: 140px; text-align: center; }
  .card--front .wordmark { font-size: 86px; padding-left: 0.5em; }
  .card--front .tagline { font-size: 17px; margin-top: 14px; }

  .band { position: absolute; left: 0; right: 0; height: 30px; background: var(--brand-red); }
  .band--top { top: 0; }
  .band--bottom { bottom: 0; }

  .card--back .brand { position: absolute; left: 45px; top: 150px; width: 290px; text-align: center; }
  .card--back .wordmark { font-size: 52px; padding-left: 0.5em; }
  .card--back .tagline { font-size: 11px; margin-top: 10px; }

  .person { position: absolute; left: 372px; top: 110px; }
  .person__name { font-family: "Tinos", serif; font-size: 24px; color: var(--brand-red); }
  .person__title { font-family: "Arimo", sans-serif; font-size: 18px; color: var(--brand-red); margin-top: 2px; }

  .contact-list { list-style: none; position: absolute; left: 365px; top: 180px; }
  .contact-list li {
    display: flex; align-items: center; height: 20px;
    font-family: "Arimo", sans-serif; font-size: 13px; color: var(--ink);
  }
  .contact-list svg { width: 14px; height: 14px; margin-right: 22px; fill: var(--brand-red); }
</style>
</head>
<body>
<main class="canvas">
  <section class="card card--front">
    <span class="edge-bar edge-bar--left"></span>
    <span class="edge-bar edge-bar--right"></span>
    <div class="brand">
      <div class="wordmark">PRCI</div>
      <p class="tagline">Plaster &amp; Resonance Craftworks Incorporated</p>
    </div>
  </section>

  <section class="card card--back">
    <span class="band band--top"></span>
    <span class="band band--bottom"></span>
    <div class="brand">
      <div class="wordmark">PRCI</div>
      <p class="tagline">Plaster &amp; Resonance Craftworks Incorporated</p>
    </div>
    <div class="person">
      <p class="person__name">Evan Hollis</p>
      <p class="person__title">Director</p>
    </div>
    <ul class="contact-list">
      <li><svg viewBox="0 0 16 16"><path d="M1 6c0-3 14-3 14 0v1h-4V5H5v2H1z M3 8h10l1 6H2z"/></svg>xxxx-xxxx</li>
      <li><svg viewBox="0 0 16 16"><path d="M8 1l7 7h-2v7h-4v-4H7v4H3V8H1z"/></svg>123 XYZ St. Sample City</li>
      <li><svg viewBox="0 0 16 16"><path d="M4 1h8v4H4z M1 6h14v9H1z M3 8v2h3V8z"/></svg>xxxx-xxxx</li>
      <li><svg viewBox="0 0 16 16"><path d="M1 3h14v10H1z" /><path d="M1 3l7 6 7-6" fill="none" stroke="#fff" stroke-width="1.5"/></svg>my_email@prci.com</li>
      <li><svg viewBox="0 0 16 16"><circle cx="8" cy="8" r="6.5" fill="none" stroke="#d40f0f" stroke-width="1.3"/><path d="M1.5 8h13 M8 1.5v13" stroke="#d40f0f" stroke-width="1.1"/><ellipse cx="8" cy="8" rx="3" ry="6.5" fill="none" stroke="#d40f0f" stroke-width="1.1"/></svg>www.prci.com</li>
    </ul>
  </section>
</main>
</body>
</html>
```